[AMAZING DESIGN NEEDED] Women's Fishing Squeeze Page

I need a professional design for a landing page that is going to collect email addresses.

You can use the creatives already on the page or you can pull images from the facebook/instagram pages.
https://www.facebook.com/LuresLinesLaces
https://www.instagram.com/lureslinesandlaces/

This is the page that needs designed: https://lureslinesandlaces-example.com/email-opt-in/

See attached for examples.

Target Market(s)

Women who like to go fishing

Industry/Entity Type

Fishing

Number of Pages Required

1 page

Font styles to use
Sans Serif

Requirements
Must have
• excellent design. Call to actions.

```html
<!DOCTYPE html>
<html lang="en">
<head>
<meta charset="utf-8">
<title>Lures, Lines & Laces — Sign Up</title>
<link rel="stylesheet" href="https://fonts.googleapis.com/css2?family=Oswald:wght@500;600&family=Plus+Jakarta+Sans:wght@400;500;600&display=swap">
<style>
:root{
  --brown:#9a7447;
  --brown-dark:#6a4f33;
  --teal:#3aa8ad;
  --tan:#c6a784;
  --ink:#222;
  --white:#fff;
}
*{box-sizing:border-box;margin:0;padding:0}
html,body{width:750px;height:1200px;overflow:hidden}
body{position:relative;font-family:"Plus Jakarta Sans",sans-serif;color:var(--ink);background:var(--white)}
.abs{position:absolute}
.head{font-family:"Oswald",sans-serif;text-transform:uppercase}
.topbar{left:0;top:0;width:750px;height:30px;background:var(--brown);color:var(--white);font-size:8px}
.topbar .item{position:absolute;top:10px;display:flex;align-items:center;gap:6px}
.sq{width:11px;height:11px;border:1.6px solid var(--white);border-radius:2px;position:absolute;top:9px}
.search{left:312px;width:80px;border-bottom:1px solid rgba(255,255,255,.5);padding-bottom:5px}
.hero{left:0;top:30px;width:750px;height:417px;background:linear-gradient(180deg,#d9e9f4 0%,#a9c6da 22%,#5f7f5a 45%,#41613f 58%,#5b7f99 70%,#345770 100%)}
.brand{left:97px;top:58px;font-size:10px;font-weight:600;color:var(--teal);width:80px;line-height:1.2}
.brand .dot{display:inline-block;width:8px;height:8px;background:var(--teal);border-radius:50%;margin-right:4px;vertical-align:-1px}
.nav{left:195px;top:64px;display:flex;gap:12px;font-size:8px;font-weight:600;color:#2a2a2a}
.callbtn{left:555px;top:53px;width:97px;height:29px;background:var(--teal);color:var(--white);display:flex;align-items:center;justify-content:center;gap:6px;font-family:"Oswald",sans-serif;font-size:12.5px;font-weight:500}
.signup{left:430px;top:122px;width:222px;height:278px;border:5px solid var(--brown);background:var(--white)}
.signup .art{left:13px;top:10px;width:33px;height:34px;background:linear-gradient(135deg,#e9c98f,#3aa8ad);border-radius:4px}
.signup h2{left:55px;top:18px;font-size:24px;font-weight:600;letter-spacing:.3px;line-height:1}
.signup h2 span{color:var(--brown)}
.signup .sub{left:13px;top:54px;font-size:10.5px;font-weight:500;letter-spacing:.7px;white-space:nowrap}
.signup .sub span{color:var(--teal)}
.signup .zig{left:0;top:78px}
.field{left:14px;width:186px;height:35px;border:1px solid #ccc;display:flex;align-items:center;padding-left:12px;gap:10px;font-size:9.5px;color:#999}
.cta{left:14px;top:222px;width:186px;height:35px;background:var(--teal);color:var(--white);font-size:14px;font-weight:500;display:flex;align-items:center;justify-content:center}
.eyebrow{left:100px;top:498px;font-size:10px;color:var(--brown);display:flex;align-items:center;gap:8px}
.eyebrow i{display:block;width:44px;height:1px;background:var(--brown)}
.about h2{position:absolute;left:98px;top:517px;font-size:20px;font-weight:600}
.copy{left:97px;top:551px;width:236px;font-size:7.6px;line-height:15px}
.copy p+p{margin-top:15px}
.learn{left:98px;top:715px;width:95px;height:33px;background:var(--teal);color:var(--white);font-size:10px;display:flex;align-items:center;justify-content:center;gap:8px;font-weight:500}
.about-photo{left:342px;top:474px;width:342px;height:302px;background:radial-gradient(ellipse at 50% 50%,#8a9a7f 0%,#2f9a98 45%,#3aa8ad 65%,rgba(58,168,173,0) 72%)}
.news{left:0;top:776px;width:750px;height:134px;background:var(--teal);color:var(--white)}
.news h3{position:absolute;left:97px;top:46px;font-family:"Oswald",sans-serif;font-size:16.5px;font-weight:500}
.news p{position:absolute;left:97px;top:78px;font-size:9px;color:#163f41}
.news .in{left:382px;top:49px;width:171px;height:38px;background:var(--white);color:#aaa;font-size:9.5px;padding-left:18px;display:flex;align-items:center}
.news .go{left:553px;top:49px;width:99px;height:38px;background:var(--brown);font-size:10px;font-weight:500;display:flex;align-items:center;justify-content:center;gap:10px}
.foot{left:0;top:910px;width:750px;height:290px;background:var(--tan)}
.col{position:absolute;top:38px}
.col h4{font-family:"Oswald",sans-serif;font-size:12px;font-weight:500;color:var(--brown-dark)}
.col h4:after{content:"";display:block;width:12px;height:1px;background:var(--brown-dark);margin-top:5px;opacity:.6}
.col ul{list-style:none;margin-top:12px;font-size:7.5px;color:#4a3623}
.col li{height:18px}
.fphone{font-family:"Oswald",sans-serif;font-size:12px;font-weight:500;color:#4a3623;display:flex;align-items:center;gap:6px;margin-top:-2px}
.socials{display:flex;gap:9px;margin-top:14px}
.socials .s{width:11px;height:11px;border:1.6px solid #4a3623;border-radius:2px}
.pay{left:0;top:201px;width:750px;height:40px;border-top:1px solid rgba(0,0,0,.08);border-bottom:1px solid rgba(0,0,0,.08)}
.pay .cell{position:absolute;top:0;height:40px;border-left:1px solid rgba(0,0,0,.08);display:flex;align-items:center;justify-content:center;font-size:10px;font-weight:600;color:#7a5f45}
.legal{left:0;top:266px;width:750px;text-align:center;font-size:6.5px;color:#4a3623}
</style>
</head>
<body>
<header class="abs topbar">
  <span class="sq" style="left:97px"></span><span class="sq" style="left:117px;border-radius:3px"></span>
  <div class="item search"><svg width="10" height="10" viewBox="0 0 10 10"><circle cx="4" cy="4" r="3" fill="none" stroke="#fff" stroke-width="1.5"/><path d="M6.3 6.3 9 9" stroke="#fff" stroke-width="1.6"/></svg>Search</div>
  <div class="item" style="left:406px"><svg width="8" height="10"><rect x="0.5" y="0.5" width="7" height="9" fill="none" stroke="#fff"/></svg>Get Certificates</div>
  <div class="item" style="left:498px"><svg width="9" height="10"><circle cx="4.5" cy="3" r="2.5" fill="#fff"/><path d="M0 10a4.5 4 0 0 1 9 0z" fill="#fff"/></svg><b>SIGN IN</b>&nbsp;or&nbsp;<b>REGISTER</b></div>
  <div class="item" style="left:606px"><svg width="11" height="10"><path d="M0 1h2l1.5 6h6l1-4.5H3" fill="none" stroke="#fff" stroke-width="1.3"/><circle cx="4" cy="9" r="1" fill="#fff"/><circle cx="9" cy="9" r="1" fill="#fff"/></svg>Cart [0]</div>
</header>

<section class="abs hero" role="img" aria-label="Photo of a woman fly fishing in a mountain lake"></section>
<div class="abs brand"><span class="dot"></span>Lures Lines &amp; Laces</div>
<nav class="abs nav"><span>CLOTHING</span><span>HATS</span><span>BUNDLES</span><span>ACCESSORIES &amp; STICKERS</span><span>JEWELRY</span><span>CLEARANCE</span></nav>
<div class="abs callbtn"><svg width="11" height="11" viewBox="0 0 24 24"><path fill="#fff" d="M6.6 10.8a15 15 0 0 0 6.6 6.6l2.2-2.2c.3-.3.7-.4 1-.2 1.1.4 2.3.6 3.6.6.6 0 1 .4 1 1V20c0 .6-.4 1-1 1A17 17 0 0 1 3 4c0-.6.4-1 1-1h3.5c.6 0 1 .4 1 1 0 1.3.2 2.5.6 3.6.1.3 0 .7-.2 1z"/></svg>4065550142</div>

<form class="abs signup">
  <div class="abs art" role="img" aria-label="Illustration of an angler with a fishing rod"></div>
  <h2 class="abs head">Sign up <span>today</span></h2>
  <div class="abs sub head">And receive <span>15% off</span> your next order</div>
  <svg class="abs zig" width="212" height="6" viewBox="0 0 212 6"><polyline fill="none" stroke="#c9b9a3" stroke-width="1" points="0,1 3,5 6,1 9,5 12,1 15,5 18,1 21,5 24,1 27,5 30,1 33,5 36,1 39,5 42,1 45,5 48,1 51,5 54,1 57,5 60,1 63,5 66,1 69,5 72,1 75,5 78,1 81,5 84,1 87,5 90,1 93,5 96,1 99,5 102,1 105,5 108,1 111,5 114,1 117,5 120,1 123,5 126,1 129,5 132,1 135,5 138,1 141,5 144,1 147,5 150,1 153,5 156,1 159,5 162,1 165,5 168,1 171,5 174,1 177,5 180,1 183,5 186,1 189,5 192,1 195,5 198,1 201,5 204,1 207,5 210,1"/></svg>
  <div class="abs field" style="top:98px"><svg width="10" height="10"><circle cx="5" cy="3" r="2.5" fill="none" stroke="#9a7447"/><path d="M.5 10a4.5 4 0 0 1 9 0" fill="none" stroke="#9a7447"/></svg>First name</div>
  <div class="abs field" style="top:138px"><svg width="10" height="10"><circle cx="5" cy="3" r="2.5" fill="none" stroke="#9a7447"/><path d="M.5 10a4.5 4 0 0 1 9 0" fill="none" stroke="#9a7447"/></svg>Last name</div>
  <div class="abs field" style="top:178px"><svg width="12" height="9"><rect x=".5" y=".5" width="11" height="8" fill="none" stroke="#9a7447"/><path d="M.5 .5 6 5l5.5-4.5" fill="none" stroke="#9a7447"/></svg>Email address *</div>
  <div class="abs cta head">Subscribe &amp; Save</div>
</form>

<section class="about">
  <div class="abs eyebrow">Who we are <i></i></div>
  <h2 class="head">About Lures Lines &amp; Laces</h2>
  <div class="abs copy">
    <p>Sed ut perspiciatis unde omnis iste natus error sit voluptatem accusantium doloremque laudantium, totam rem aperiam, eaque ipsa quae ab illo inventore veritatis et quasi architecto beatae vitae dicta sunt explicabo. Nemo enim ipsam voluptatem quia volup.</p>
    <p>Neque porro quisquam est, qui dolorem ipsum quia dolor sit amet, consectetur, adipisci velit, sed quia non numquam eius modi tempora incidunt ut labore et dolore magnam aliquam quaerat voluptatem.</p>
  </div>
  <div class="abs learn head">Learn more <svg width="10" height="6"><path d="M0 3h9M6.5.5 9 3 6.5 5.5" fill="none" stroke="#fff"/></svg></div>
  <div class="abs about-photo" role="img" aria-label="Photo of a smiling angler holding a rainbow trout over a teal paint splash"></div>
</section>

<section class="abs news">
  <h3>Subscribe to Our Newsletter</h3>
  <p>Get the latest updates on new products and upcoming sales</p>
  <div class="abs in">Your Email address</div>
  <div class="abs go head">Subscribe <svg width="16" height="14" viewBox="0 0 16 14"><path d="M16 0 0 6l5 2 1 6 3-4 4 3z" fill="none" stroke="#fff"/></svg></div>
</section>

<footer class="abs foot">
  <div class="col" style="left:97px"><h4>Navigate</h4><ul><li>Trips</li><li>Shipping &amp; Returns</li><li>Contact Us</li><li>Blog</li><li>Sitemap</li></ul></div>
  <div class="col" style="left:240px"><h4>Categories</h4><ul><li>Clothing</li><li>Hats</li><li>Bundles</li><li>Accessories &amp; Stickers</li><li>Jewelry</li><li>Clearance</li></ul></div>
  <div class="col" style="left:383px"><h4>Info</h4><ul><li>Montana</li></ul>
    <div class="fphone"><svg width="10" height="10" viewBox="0 0 24 24"><path fill="#4a3623" d="M6.6 10.8a15 15 0 0 0 6.6 6.6l2.2-2.2c.3-.3.7-.4 1-.2 1.1.4 2.3.6 3.6.6.6 0 1 .4 1 1V20c0 .6-.4 1-1 1A17 17 0 0 1 3 4c0-.6.4-1 1-1h3.5c.6 0 1 .4 1 1 0 1.3.2 2.5.6 3.6.1.3 0 .7-.2 1z"/></svg>4065550142</div></div>
  <div class="col" style="left:525px"><h4>Connect With Us</h4><div class="socials"><span class="s"></span><span class="s"></span></div></div>
  <div class="abs pay">
    <div class="cell" style="left:97px;width:110px">Northcard</div>
    <div class="cell" style="left:207px;width:116px">Rivercard</div>
    <div class="cell" style="left:323px;width:115px">Troutpay</div>
    <div class="cell" style="left:438px;width:103px">Creekpay</div>
    <div class="cell" style="left:541px;width:111px;border-right:1px solid rgba(0,0,0,.08)">Ridgecard</div>
  </div>
  <div class="abs legal">Copyright © 2021 Lures, Lines &amp; Laces. All rights reserved</div>
</footer>
</body>
</html>
```